Salon Signage

We need a new company sign designed for the exterior of our salon. I have attached our current logos for an idea. I have also attached a photo of what salon looks like currently.

```html
<!DOCTYPE html>
<html lang="en">
<head>
<meta charset="utf-8">
<title>Velvet Locks Beauty Salon – Exterior Sign</title>
<link href="https://fonts.googleapis.com/css2?family=Montserrat:wght@500;800&display=swap" rel="stylesheet">
<style>
  :root {
    --page: #e9e9eb;
    --sign: #ffffff;
    --ink: #111111;
    --magenta: #d1127f;
    --magenta-deep: #8e1a7a;
    --band-dark: #0c0c0c;
    --photo-a: #c9a08a;
    --photo-b: #4a3530;
  }
  * { margin: 0; padding: 0; box-sizing: border-box; }
  html, body { width: 756px; height: 1200px; overflow: hidden; }
  body {
    background: var(--page);
    font-family: "Montserrat", Arial, sans-serif;
    display: flex;
    align-items: center;
    justify-content: center;
  }
  .sign {
    width: 716px;
    height: 150px;
    background: var(--sign);
    display: flex;
    flex-direction: column;
    box-shadow: 0 2px 8px rgba(0,0,0,0.12);
  }
  .sign-top {
    flex: 1;
    display: flex;
    align-items: center;
    padding: 0 26px 0 30px;
  }
  .brand {
    display: flex;
    align-items: center;
    gap: 16px;
  }
  .brand-mark {
    width: 70px;
    height: 70px;
    border-radius: 50%;
    background: var(--magenta);
    flex: none;
  }
  .brand-name {
    font-weight: 800;
    color: var(--ink);
    font-size: 38px;
    line-height: 0.95;
    letter-spacing: -0.5px;
    text-transform: uppercase;
  }
  .brand-name small {
    display: block;
    font-size: 22px;
    letter-spacing: 0.5px;
    margin-top: 4px;
  }
  .portrait {
    margin-left: auto;
    width: 96px;
    height: 96px;
    border-radius: 50%;
    border: 3px solid var(--magenta);
    background: radial-gradient(circle at 50% 40%, var(--photo-a), var(--photo-b));
  }
  .sign-band {
    height: 30px;
    display: flex;
    color: #fff;
    font-size: 14px;
    font-weight: 500;
  }
  .band-web {
    flex: 0 0 66%;
    background: linear-gradient(90deg, var(--magenta-deep), var(--magenta));
    display: flex;
    align-items: center;
    gap: 8px;
    padding-left: 30px;
    letter-spacing: 0.3px;
  }
  .band-phone {
    flex: 1;
    background: var(--band-dark);
    display: flex;
    align-items: center;
    justify-content: center;
    gap: 10px;
    font-size: 19px;
    font-weight: 800;
    letter-spacing: 0.5px;
  }
  .icon { width: 16px; height: 16px; flex: none; }
</style>
</head>
<body>
  <div class="sign">
    <div class="sign-top">
      <div class="brand">
        <span class="brand-mark"></span>
        <div class="brand-name">Velvet Locks<small>Beauty Salon</small></div>
      </div>
      <div class="portrait" role="img" aria-label="Round portrait photo of the salon stylist"></div>
    </div>
    <div class="sign-band">
      <div class="band-web">
        <svg class="icon" viewBox="0 0 16 16" aria-hidden="true">
          <circle cx="8" cy="8" r="7" fill="#fff"/>
          <path d="M6.5 5 L10 8 L6.5 11" stroke="#d1127f" stroke-width="1.8" fill="none"/>
        </svg>
        <span>www.velvetlockssalon.business.site</span>
      </div>
      <div class="band-phone">
        <svg class="icon" viewBox="0 0 16 16" aria-hidden="true">
          <circle cx="8" cy="8" r="8" fill="#fff"/>
          <path d="M5.2 3.8l1.5 1.6-.8 1.2c.6 1.3 1.5 2.2 2.8 2.8l1.2-.8 1.6 1.5-.9 1.5c-3.2-.3-5.9-3-6.2-6.2z" fill="#0c0c0c"/>
        </svg>
        <span>9140 5527</span>
      </div>
    </div>
  </div>
</body>
</html>
```